QM Kalorvex.Brendal GmbH needed a letterhead template

For English scroll down. We need a letterhead template and since we already have our logo design successfully with you, we now want to also design the letterhead with you. Down in the uploaded file you see what is important and what should definitely be seen on our template. The template should be like the homepage (www.kalorvex.brendal) held in red, blue and white. We need a letter-head submission. In the bottom in the chapter "databases uploading" you can find the most important things, did must be on the submission. The submission shoulderstand be in the colors blue, red and white like our homepage (www.kalorvex.brendal).

```html
<!DOCTYPE html>
<html lang="de">
<head>
<meta charset="utf-8">
<title>Kalorvex.Brendal – Briefpapier</title>
<link href="https://fonts.googleapis.com/css2?family=Open+Sans:wght@400;600;700&display=swap" rel="stylesheet">
<style>
  :root {
    --brand-blue: #3d86cf;
    --brand-red: #d7262f;
    --charcoal: #2f3133;
    --paper: #ffffff;
    --backdrop: #e3e4e6;
    --text: #3b3d40;
  }
  * { box-sizing: border-box; margin: 0; padding: 0; }
  html, body { width: 1200px; height: 800px; overflow: hidden; }
  body {
    background: var(--backdrop);
    font-family: "Open Sans", Arial, sans-serif;
    color: var(--text);
    position: relative;
  }
  .letterhead {
    position: absolute;
    left: 331px; top: 20px;
    width: 538px; height: 760px;
    background: var(--paper);
    box-shadow: 0 6px 18px rgba(0,0,0,.12);
    overflow: hidden;
  }
  .top-band { position: absolute; left: 0; top: 0; width: 100%; height: 14px; background: var(--brand-blue); }
  .top-rule { position: absolute; left: 0; top: 14px; width: 100%; height: 5px; background: var(--charcoal); }

  .brand {
    position: absolute; left: 44px; top: 52px;
    display: flex; align-items: center; gap: 8px;
  }
  .brand-dot { width: 22px; height: 22px; border-radius: 50%; background: var(--brand-blue); }
  .brand-name { font-weight: 700; font-size: 20px; color: var(--brand-red); letter-spacing: -.2px; }

  .letter-date {
    position: absolute; right: 44px; top: 118px;
    font-size: 8.5px; letter-spacing: .3px; text-transform: uppercase;
  }
  .recipient { position: absolute; left: 44px; top: 142px; font-size: 10px; line-height: 1.45; font-style: normal; }
  .letter-body {
    position: absolute; left: 44px; top: 200px; width: 450px;
    font-size: 8.5px; line-height: 1.55;
  }
  .letter-body p + p { margin-top: 11px; }

  .closing { position: absolute; left: 44px; top: 540px; font-size: 10px; }
  .signature-area {
    display: block; width: 44px; height: 18px; margin: 8px 0 6px 10px;
    background: linear-gradient(90deg, #d8d9db, #eeeeef); border-radius: 3px;
  }
  .signer { font-size: 9px; letter-spacing: .4px; text-transform: uppercase; }

  .footer-band { position: absolute; left: 0; top: 680px; width: 100%; height: 52px; background: var(--brand-blue); }
  .footer-rule { position: absolute; left: 0; top: 738px; width: 100%; height: 5px; background: var(--charcoal); }
  .footer-base { position: absolute; left: 0; top: 743px; width: 100%; height: 17px; background: var(--brand-blue); }

  .contact {
    position: absolute; display: flex; align-items: center; gap: 8px;
    color: #fff; font-size: 7px; line-height: 1.55; padding-left: 16px;
    white-space: nowrap;
  }
  .contact-phone { left: 0; top: 680px; width: 210px; height: 52px; }
  .contact-online { left: 210px; top: 664px; width: 178px; height: 68px; background: var(--charcoal); padding-left: 12px; }
  .contact-address { left: 388px; top: 650px; width: 150px; height: 82px; background: var(--brand-blue); padding-left: 12px; }
  .contact-icon {
    flex: none; width: 20px; height: 20px; background: #fff; border-radius: 3px;
    display: flex; align-items: center; justify-content: center;
  }
  .contact-icon svg { width: 13px; height: 13px; fill: var(--charcoal); }
</style>
</head>
<body>
  <main class="letterhead">
    <div class="top-band"></div>
    <div class="top-rule"></div>

    <header class="brand">
      <span class="brand-dot"></span>
      <span class="brand-name">Kalorvex.Brendal</span>
    </header>

    <div class="letter-date">Date : 20 May 2020</div>

    <address class="recipient">
      Geschäftsführer<br>Dr. Vostrich Marlen
    </address>

    <section class="letter-body">
      <p>There are many variations of passages of Lorem Ipsum available, but the majority have suffered alteration in some form, by injected humour, or randomised words which don't look even slightly believable. If you are going to use a passage of Lorem Ipsum, you need to be sure there isn't anything embarrassing hidden in the middle of text. All the Lorem Ipsum generators on the Internet tend to repeat predefined chunks as necessary, making this the first true generator on the Internet. It uses a dictionary of over 200 Latin words.</p>
      <p>Combined with a handful of model sentence structures, to generate Lorem Ipsum which looks reasonable. The generated Lorem Ipsum is therefore always free from repetition, injected humour, or non-characteristic words etc. All the Lorem Ipsum generators on the Internet tend to repeat predefined chunks as necessary, making.</p>
      <p>There are many variations of passages of Lorem Ipsum available, but the majority have suffered alteration in some form, by injected humour, or randomised words which don't look even slightly believable. If you are going to use a passage.</p>
    </section>

    <div class="closing">
      <p>Sincerely yours,</p>
      <span class="signature-area" role="img" aria-label="Handwritten signature"></span>
      <p class="signer">Lukas Fernow</p>
    </div>

    <div class="footer-band"></div>
    <div class="footer-rule"></div>
    <div class="footer-base"></div>

    <div class="contact contact-phone">
      <span class="contact-icon"><svg viewBox="0 0 24 24"><path d="M6.6 10.8a15.5 15.5 0 0 0 6.6 6.6l2.2-2.2c.3-.3.7-.4 1-.2 1.1.4 2.3.6 3.6.6.6 0 1 .4 1 1V20c0 .6-.4 1-1 1A17 17 0 0 1 3 4c0-.6.4-1 1-1h3.5c.6 0 1 .4 1 1 0 1.3.2 2.5.6 3.6.1.3 0 .7-.2 1z"/></svg></span>
      <span>0800 XX XX XX</span>
    </div>

    <div class="contact contact-online">
      <span class="contact-icon"><svg viewBox="0 0 24 24"><path d="M3 5h18v14H3zm2 2v.5l7 4.5 7-4.5V7zm0 2.8V17h14V9.8l-7 4.5z"/></svg></span>
      <span>Mail: contact@kalorvex.brendal<br>Web: www.kalorvex.brendal</span>
    </div>

    <div class="contact contact-address">
      <span class="contact-icon"><svg viewBox="0 0 24 24"><path d="M12 2a7 7 0 0 0-7 7c0 5.2 7 13 7 13s7-7.8 7-13a7 7 0 0 0-7-7zm0 9.5A2.5 2.5 0 1 1 12 6.5a2.5 2.5 0 0 1 0 5z"/></svg></span>
      <span>Weidgasse 4<br>6020 Feldau, Tirol<br>Österreich</span>
    </div>
  </main>
</body>
</html>
```